Business Card Design for Lawn Management

Lawn Management

Industry/Entity Type

Business

Contact Information for Business Card

Calloway Lawn Management
Joel Calloway
Calloway_Lawn@brindlemail.com
404-555-0172

```html
<!DOCTYPE html>
<html lang="en">
<head>
<meta charset="utf-8">
<title>Calloway Lawn Management — Business Card</title>
<link rel="stylesheet" href="https://fonts.googleapis.com/css2?family=Teko:wght@400;500;600&display=swap">
<style>
  :root {
    --page-bg: #e9e4dc;
    --paper: #f4f4f2;
    --grass-light: #4a9a34;
    --grass-mid: #2f7d22;
    --grass-dark: #1f5e16;
    --brand-green: #2e8b2e;
    --brand-border: #2a8a2a;
    --back-top: #3a9a3c;
    --back-bottom: #1f6e26;
    --back-ink: #1e5c22;
    --white: #ffffff;
  }
  * { box-sizing: border-box; margin: 0; padding: 0; }
  html, body {
    width: 1200px;
    height: 905px;
    overflow: hidden;
    background: var(--page-bg);
    font-family: "Teko", "Arial Narrow", sans-serif;
  }
  .canvas {
    position: relative;
    width: 1200px;
    height: 905px;
  }
  .card {
    position: absolute;
    width: 616px;
    height: 356px;
    overflow: hidden;
    box-shadow: 0 3px 8px rgba(0,0,0,0.35);
  }
  /* Front side */
  .card-front {
    left: 64px;
    top: 104px;
    z-index: 2;
  }
  .grass-field {
    position: absolute;
    inset: 0;
    background: radial-gradient(ellipse at 60% 40%, var(--grass-light), var(--grass-mid) 55%, var(--grass-dark));
  }
  .brand-panel {
    position: absolute;
    inset: 0;
    width: 616px;
    height: 356px;
  }
  .brand-name {
    position: absolute;
    left: 30px;
    top: 150px;
    width: 220px;
    color: var(--brand-green);
    font-weight: 500;
    text-align: center;
    line-height: 0.9;
  }
  .brand-name .brand-main {
    display: block;
    font-size: 52px;
    letter-spacing: 1px;
  }
  .brand-name .brand-sub {
    display: block;
    font-size: 27px;
  }
  .brand-mark {
    position: absolute;
    left: 112px;
    top: 80px;
    width: 56px;
    height: 56px;
    border-radius: 50%;
    background: var(--brand-green);
  }
  .contact {
    position: absolute;
    left: 250px;
    width: 340px;
    text-align: center;
    color: var(--white);
    text-shadow: 0 1px 2px rgba(0,0,0,0.5);
    letter-spacing: 1.5px;
    white-space: nowrap;
  }
  .contact-name { top: 38px; font-size: 38px; font-weight: 400; }
  .contact-phone { top: 82px; font-size: 30px; font-weight: 400; }
  .contact-email { top: 280px; font-size: 24px; font-weight: 400; letter-spacing: 0.5px; }

  /* Back side */
  .card-back {
    left: 574px;
    top: 421px;
    z-index: 1;
    background: linear-gradient(180deg, var(--back-top), var(--back-bottom));
  }
  .back-mark {
    position: absolute;
    left: 278px;
    top: 100px;
    width: 60px;
    height: 60px;
    border-radius: 50%;
    background: var(--back-ink);
  }
  .back-name {
    position: absolute;
    left: 0;
    top: 180px;
    width: 616px;
    text-align: center;
    color: var(--back-ink);
    font-weight: 500;
    line-height: 0.9;
  }
  .back-name .brand-main { display: block; font-size: 56px; letter-spacing: 1px; }
  .back-name .brand-sub { display: block; font-size: 28px; }
</style>
</head>
<body>
<main class="canvas">
  <section class="card card-front" aria-label="Business card front">
    <div class="grass-field" role="img" aria-label="Close-up photograph of green lawn grass"></div>
    <svg class="brand-panel" viewBox="0 0 616 356" aria-hidden="true">
      <path d="M0 0 H212 Q300 170 218 356 H0 Z" fill="var(--brand-border)"/>
      <path d="M0 0 H200 Q286 170 206 356 H0 Z" fill="var(--paper)"/>
    </svg>
    <span class="brand-mark" aria-hidden="true"></span>
    <p class="brand-name">
      <span class="brand-main">CALLOWAY</span>
      <span class="brand-sub">Lawn Management</span>
    </p>
    <p class="contact contact-name">Joel Calloway</p>
    <p class="contact contact-phone">404-555-0172</p>
    <p class="contact contact-email">Calloway_Lawn@brindlemail.com</p>
  </section>

  <section class="card card-back" aria-label="Business card back">
    <span class="back-mark" aria-hidden="true"></span>
    <p class="back-name">
      <span class="brand-main">CALLOWAY</span>
      <span class="brand-sub">Lawn Management</span>
    </p>
  </section>
</main>
</body>
</html>
```